Full re-design of visual identity

We have just re-designed our logo and would like to apply it on our folders, business cards, stationery, and etc... we are attaching new logo + the material we need to re-design... we will provide full corel draw files to help make job easier and also because lot of icons and artwork can be still used...

any doubts we are at your disposal. thanks in advance.

Business

```html
<!DOCTYPE html>
<html lang="en">
<head>
<meta charset="utf-8">
<title>Orvalink Stationery Set</title>
<link href="https://fonts.googleapis.com/css2?family=Titillium+Web:wght@400;700&family=Tinos:wght@400&display=swap" rel="stylesheet">
<style>
  :root {
    --bg: #efefef;
    --paper: #f7f7f7;
    --paper-edge: #e2e2e2;
    --orange: #e0620f;
    --orange-deep: #c4500d;
    --ink: #5a5a5a;
    --text: #222;
    --muted: #888;
  }
  * { box-sizing: border-box; margin: 0; padding: 0; }
  html, body { width: 1200px; height: 795px; overflow: hidden; }
  body { background: var(--bg); position: relative; font-family: "Titillium Web", sans-serif; }

  .piece { position: absolute; background: var(--paper); box-shadow: 0 1px 2px rgba(0,0,0,.12); overflow: hidden; }

  .brand { display: inline-flex; align-items: center; gap: .25em; font-family: "Titillium Web", sans-serif; font-weight: 700; color: var(--ink); line-height: 1; }
  .brand .dot { width: .5em; height: .5em; border-radius: 50%; background: var(--orange); display: inline-block; }
  .brand--white { color: #fff; }
  .brand--white .dot { background: #fff; }
  .tagline { font-size: 5px; color: var(--muted); letter-spacing: .3px; margin-top: 2px; }

  /* Letterhead */
  .letterhead { left: 298px; top: 38px; width: 275px; height: 370px; }
  .letterhead .brand { position: absolute; left: 44px; top: 18px; font-size: 22px; }
  .letterhead .tagline { position: absolute; left: 44px; top: 40px; }
  .letter { position: absolute; left: 38px; top: 88px; width: 200px; font-family: "Tinos", serif; font-size: 5.2px; line-height: 1.45; color: var(--text); text-align: justify; }
  .letter p { margin-bottom: 6px; }
  .signature { width: 40px; height: 10px; background: linear-gradient(90deg, #bdbdbd, #d8d8d8); margin: 2px 0; }
  .contact-list { position: absolute; left: 24px; top: 322px; list-style: none; font-size: 4.2px; color: var(--muted); line-height: 1.9; }
  .contact-list li::before { content: ""; display: inline-block; width: 3px; height: 3px; border-radius: 50%; background: var(--orange); margin-right: 6px; vertical-align: middle; }
  .band { position: absolute; left: 0; bottom: 0; width: 100%; height: 16px; }

  /* Folder */
  .folder { left: 597px; top: 36px; width: 303px; height: 384px; background: linear-gradient(160deg, var(--orange) 0%, var(--orange-deep) 100%); }
  .folder .brand { position: absolute; left: 94px; top: 164px; font-size: 34px; }
  .folder .tagline { position: absolute; left: 96px; top: 200px; color: #ffe3cf; font-size: 5.5px; }

  /* Business cards */
  .card { top: 436px; width: 120px; height: 64px; }
  .card--front { left: 296px; }
  .card--front .brand { position: absolute; left: 14px; top: 8px; font-size: 14px; }
  .card--front .holder { position: absolute; right: 12px; top: 26px; text-align: left; font-size: 4.6px; color: var(--text); }
  .card--front .holder span { display: block; color: var(--orange); }
  .card--front .contact-list { left: 8px; top: 26px; font-size: 3.2px; line-height: 1.8; }
  .card--front .band { height: 6px; }
  .card--back { left: 454px; width: 119px; background: linear-gradient(160deg, var(--orange), var(--orange-deep)); display: flex; align-items: center; justify-content: center; }
  .card--back .brand { font-size: 13px; }

  /* Envelopes */
  .envelope { left: 613px; top: 447px; width: 287px; height: 115px; }
  .envelope .flap { position: absolute; inset: 0; }
  .envelope .brand { position: absolute; left: 124px; top: 12px; font-size: 13px; }
  .dl-envelope { left: 613px; top: 612px; width: 292px; height: 148px; }
  .dl-envelope .brand { position: absolute; left: 30px; top: 20px; font-size: 22px; }
  .dl-envelope .tagline { position: absolute; left: 32px; top: 43px; }

  /* Notebook */
  .notebook { left: 316px; top: 562px; width: 112px; height: 202px; }
  .notebook .spiral { position: absolute; left: 3px; top: 6px; bottom: 6px; width: 4px; background: repeating-linear-gradient(180deg, #444 0 2px, transparent 2px 5px); }
  .notebook .brand { position: absolute; left: 10px; top: 90px; font-size: 17px; }
  .notebook .tagline { position: absolute; left: 11px; top: 108px; font-size: 4px; }

  /* Key tag & eraser */
  .key-tag { left: 465px; top: 570px; width: 42px; height: 84px; border-radius: 6px; display: flex; align-items: center; justify-content: center; }
  .key-tag .brand { font-size: 9px; }
  .eraser { left: 479px; top: 682px; width: 24px; height: 64px; display: flex; align-items: center; justify-content: center; }
  .eraser .dot { width: 9px; height: 9px; border-radius: 50%; background: var(--orange); }
</style>
</head>
<body>

<section class="piece letterhead">
  <div class="brand">orvalink<span class="dot"></span></div>
  <div class="tagline">telecom · tecnologia · internet</div>
  <article class="letter">
    <p>Gentlemen,</p>
    <p>Enclosed please find the proposal we discussed last week regarding the new network service for your offices. We would be pleased if you could review it at your convenience and share any remarks before the end of the month. Our team is ready to begin installation as soon as the terms are agreed, and we will keep you informed at every stage of the work.</p>
    <p>Should you wish to change any part of the plan, simply let us know and we will prepare a revised version. We thank you for your trust and look forward to a long and productive partnership with your company.</p>
    <p style="margin-top:26px;margin-bottom:0">In the meantime I remain<br>Yours very truly,</p>
    <div class="signature" role="img" aria-label="Handwritten signature"></div>
    <p>Elias Marren</p>
  </article>
  <ul class="contact-list">
    <li>(972) 555-0142</li>
    <li>(972) 555-0187</li>
    <li>hello@orvalink.com</li>
    <li>www.orvalink.com</li>
  </ul>
  <svg class="band" viewBox="0 0 275 16" preserveAspectRatio="none">
    <path d="M0 8 Q137 -2 275 8 L275 16 L0 16 Z" fill="var(--orange)"/>
  </svg>
</section>

<section class="piece folder">
  <div class="brand brand--white">orvalink<span class="dot"></span></div>
  <div class="tagline">telecom · tecnologia · internet</div>
</section>

<section class="piece card card--front">
  <div class="brand">orvalink<span class="dot"></span></div>
  <ul class="contact-list">
    <li>(972) 555-0142</li>
    <li>(972) 555-0187</li>
    <li>dana@orvalink.com</li>
    <li>www.orvalink.com</li>
  </ul>
  <div class="holder">Dana Ross<span>Producer</span></div>
  <svg class="band" viewBox="0 0 120 6" preserveAspectRatio="none">
    <path d="M0 3 Q60 -1 120 3 L120 6 L0 6 Z" fill="var(--orange)"/>
  </svg>
</section>

<section class="piece card card--back">
  <div class="brand brand--white">orvalink<span class="dot"></span></div>
</section>

<section class="piece envelope">
  <svg class="flap" viewBox="0 0 287 115" preserveAspectRatio="none">
    <path d="M0 0 L10 48 L277 48 L287 0" fill="none" stroke="var(--paper-edge)" stroke-width="1"/>
  </svg>
  <div class="brand">orvalink<span class="dot"></span></div>
</section>

<section class="piece dl-envelope">
  <div class="brand">orvalink<span class="dot"></span></div>
  <div class="tagline">telecom · tecnologia · internet</div>
</section>

<section class="piece notebook">
  <div class="spiral"></div>
  <div class="brand">orvalink<span class="dot"></span></div>
  <div class="tagline">telecom · tecnologia · internet</div>
</section>

<section class="piece key-tag">
  <div class="brand">orvalink<span class="dot"></span></div>
</section>

<section class="piece eraser">
  <span class="dot"></span>
</section>

</body>
</html>
```